Disability and mental health support work company requires business card

Specialising
Bellwind Disability is a new HVTA service aimed toward HVTA participants with a history of criminal justice, psychosocial/mental health, intellectual, and cognitive disabilities.

Our focus
Focusing on providing core HVTA supports for community participation, daily activities and supported independent living.

Authentic
Likeminded people wanting to make a difference in participant's lives.

Our aim to provide holistic and empowering supports targeted towards creating independence and guidance for all participants and families.
Over 35 years of experience working with people that have psychosocial, intellectual, and cognitive disabilities.

Industry/Entity Type

disability and mental health

Contact Information for Business Card

logo - business name

Colors
0054AA
0677BA
7BADD7
CADEEF
E8F1F8
FFF300
FFF600
FEFA6F
FFFEC7
FFFEE8

Requirements
Must have
• want double sided business cards(wont let me change it)
Should not have
• any disability related pictures

```html
<!DOCTYPE html>
<html lang="en">
<head>
<meta charset="utf-8">
<title>Bellwind Disability – Business Card</title>
<link href="https://fonts.googleapis.com/css2?family=Montserrat:wght@400;500;700;800&display=swap" rel="stylesheet">
<style>
  :root {
    --page: #e8e9eb;
    --rule: #cfd1d4;
    --card: #12375e;
    --sky: #7badd7;
    --gold: #f0b323;
    --white: #ffffff;
  }
  * { margin: 0; padding: 0; box-sizing: border-box; }
  html, body { width: 1047px; height: 1200px; overflow: hidden; }
  body {
    position: relative;
    background: var(--page);
    font-family: "Montserrat", Arial, sans-serif;
    color: var(--white);
  }
  .top-rule {
    position: absolute; left: 352px; top: 51px; width: 609px; height: 1px;
    background: var(--rule);
  }
  .card {
    position: absolute; width: 843px; height: 481px;
    background: var(--card);
    box-shadow: 0 8px 30px rgba(0,0,0,0.28);
  }
  .card--front { left: 84px; top: 87px; }
  .card--back { left: 77px; top: 622px; }

  .accent-bar {
    position: absolute; left: 0; top: 88px; width: 10px; height: 55px;
    background: var(--gold);
  }
  .person-name {
    position: absolute; left: 39px; top: 84px;
    font-size: 35px; font-weight: 800; letter-spacing: -0.06em;
    color: var(--sky); line-height: 1; white-space: nowrap;
  }
  .person-role {
    position: absolute; left: 37px; top: 124px;
    font-size: 23px; font-weight: 400; line-height: 1.2;
  }
  .contact-list { position: absolute; left: 45px; top: 274px; list-style: none; }
  .contact-item {
    display: flex; align-items: center; height: 31px;
    font-size: 22px; font-weight: 400;
  }
  .contact-item:nth-child(3) { height: 28px; }
  .contact-icon { width: 21px; height: 21px; margin-right: 13px; flex: none; }
  .address {
    position: absolute; left: 44px; top: 376px;
    font-size: 23px; line-height: 33px; font-style: normal;
  }

  .brand-ring {
    position: absolute; border-radius: 50%;
    border: 1.2px solid var(--sky);
    box-shadow: 0 6px 24px rgba(0,0,0,0.35);
    display: flex; align-items: center; justify-content: center;
  }
  .card--front .brand-ring { left: 418px; top: 44px; width: 392px; height: 394px; }
  .card--back .brand-ring { left: 239px; top: 60px; width: 364px; height: 366px; }
  .brand-name {
    text-align: center; color: var(--sky);
    font-weight: 700; text-transform: uppercase; line-height: 1.1;
  }
  .card--front .brand-name { font-size: 38px; letter-spacing: 0.02em; }
  .card--back .brand-name { font-size: 35px; letter-spacing: 0.02em; }
</style>
</head>
<body>
  <div class="top-rule"></div>

  <section class="card card--front">
    <div class="accent-bar"></div>
    <h1 class="person-name">MARCUS ELLERY</h1>
    <p class="person-role">Managing Director</p>

    <ul class="contact-list">
      <li class="contact-item">
        <svg class="contact-icon" viewBox="0 0 24 24" aria-hidden="true">
          <path fill="var(--gold)" d="M6.6 2.5l3 3.6c.4.5.4 1.2 0 1.7L8.2 9.4c1.2 2.6 3.3 4.8 6 6l1.6-1.4c.5-.4 1.2-.4 1.7 0l3.6 3c.5.4.6 1.2.1 1.7l-1.9 2.2c-.6.6-1.5.9-2.4.6C9.6 19.4 4.6 14.4 2.5 7.1c-.3-.9 0-1.8.6-2.4l1.8-2.1c.5-.5 1.3-.5 1.7-.1z"/>
          <path fill="none" stroke="var(--gold)" stroke-width="1.6" stroke-linecap="round" d="M14 3.5a7 7 0 0 1 6.5 6.5M13.8 7a3.6 3.6 0 0 1 3.2 3.2"/>
        </svg>
        044-987 650 312
      </li>
      <li class="contact-item">
        <svg class="contact-icon" viewBox="0 0 24 24" aria-hidden="true">
          <rect x="1" y="5" width="22" height="15" fill="var(--gold)"/>
          <path d="M1 5l11 8.5L23 5M1 20l8.5-7.5M23 20l-8.5-7.5" fill="none" stroke="var(--card)" stroke-width="1.3"/>
        </svg>
        info@bellwind.com
      </li>
      <li class="contact-item">
        <svg class="contact-icon" viewBox="0 0 24 24" aria-hidden="true">
          <circle cx="12" cy="12" r="10" fill="none" stroke="var(--gold)" stroke-width="2"/>
          <path fill="var(--gold)" d="M6 7c2-1 4-.5 5 1s-1 3-2.5 3-1 2-2.5 2.5S4 11 5 9zM13 13c2-.5 4 .5 4 2.5s-2 4-3.5 4.5-1-2.5-1.5-4 0-2.8 1-3zM14 5c2 0 4 1.5 4.5 3s-2 1-3 .5-2.5-3.5-1.5-3.5z"/>
        </svg>
        www.bellwindcare.com
      </li>
    </ul>

    <address class="address">
      17, Harbour View Lane<br>
      Eastbrook Vale, 48120
    </address>

    <div class="brand-ring">
      <p class="brand-name">Bellwind<br>Disability</p>
    </div>
  </section>

  <section class="card card--back">
    <div class="brand-ring">
      <p class="brand-name">Bellwind<br>Disability</p>
    </div>
  </section>
</body>
</html>
```